brookline diner & tap

menu design contracting menu to two views. reducing number of offerings. website. http://brooklinediner-ferrowave.com/brooklinemenu.html
have reduced our menu offering by 25 items to achieve a 2 view profile vs our current 5 view look. 8 1/2 x 11 preferred but 8 1/2 by 14 possible. Would like to employ a menu board concept but sleeves will also be a considered option.

Target Market(s)

families, blue collar, home style, meat loaf, fried chicken, burgers, chicken fried steak etc

Industry/Entity Type

American Restaurant

Font styles to use
Sans Serif

Colors
f68e4d
faa54b
fece3e
fbee3e
aaaaaa
9d9d9d
b1b1b1
1b1b1b

Requirements
Must have
• 2 views
Nice to have
• colors
Should not have
• clutter, unstructured,

```html
<!DOCTYPE html>
<html lang="en">
<head>
<meta charset="utf-8">
<title>Brookline Diner &amp; Tap — Menu</title>
<link rel="stylesheet" href="https://fonts.googleapis.com/css2?family=Roboto+Condensed:wght@400;700&family=Yellowtail&family=Josefin+Slab:wght@700&family=Raleway:wght@500&display=swap">
<style>
  :root {
    --paper: #efe5cd;
    --paper-edge: #c9b48f;
    --red: #c0282c;
    --red-deep: #8e1c20;
    --ink: #1b1b1b;
    --meat: #b9846a;
    --greens: #8fae6a;
    --band: #c4262b;
  }
  * { margin: 0; padding: 0; box-sizing: border-box; }
  html, body { width: 928px; height: 1200px; overflow: hidden; }
  body {
    position: relative;
    background: radial-gradient(ellipse at 50% 45%, #f3ead5 0%, var(--paper) 55%, var(--paper-edge) 100%);
    font-family: "Roboto Condensed", "Arial Narrow", sans-serif;
    color: var(--ink);
  }
  .brand {
    position: absolute; top: 72px; left: 0; width: 928px;
    text-align: center;
    font-family: "Roboto Condensed", sans-serif; font-weight: 700;
    font-size: 34px; color: var(--red-deep); letter-spacing: 1px;
  }
  .section-kicker {
    position: absolute; top: 168px; left: 0; width: 928px; text-align: center;
    font-family: "Yellowtail", cursive; font-size: 52px; color: var(--red);
    line-height: 1;
  }
  .section-title {
    position: absolute; top: 222px; left: 0; width: 928px; text-align: center;
    font-family: "Josefin Slab", serif; font-weight: 700;
    font-size: 46px; letter-spacing: 5px; color: var(--red);
    text-shadow: 2px 2px 0 #e9c9b8, 3px 3px 0 var(--red-deep);
  }
  .column { position: absolute; }
  .steak-left { left: 58px; top: 314px; width: 372px; }
  .steak-right { left: 480px; top: 314px; width: 386px; }
  .item { margin-bottom: 15px; }
  .item-head {
    display: flex; justify-content: space-between;
    font-weight: 700; font-size: 15px; color: var(--red); text-transform: uppercase;
    line-height: 1.15;
  }
  .item-desc { font-size: 13.4px; line-height: 1.22; text-transform: uppercase; }
  .steak-art {
    position: absolute; left: 462px; top: 398px; width: 426px; height: 212px;
    border-radius: 40% 45% 20% 30%;
    background: radial-gradient(ellipse at 55% 45%, #d69a8a 0%, var(--meat) 45%, #b7a46a 75%, rgba(185,160,110,0) 100%);
  }
  .served-note {
    position: absolute; left: 486px; top: 634px; width: 400px;
    display: flex; gap: 10px; align-items: flex-start;
    font-weight: 700; font-size: 15px; color: var(--red); text-transform: uppercase; line-height: 1.2;
  }
  .band {
    position: absolute; left: 30px; top: 714px; width: 868px; height: 56px;
    background: var(--band);
    color: #f3e8d4; text-align: center;
    font-family: "Raleway", sans-serif; font-weight: 500;
    font-size: 38px; letter-spacing: 6px; line-height: 56px;
  }
  .salad-frame {
    position: absolute; left: 30px; top: 770px; width: 868px; height: 388px;
    border: 1.5px solid var(--band); border-top: none;
  }
  .salad-left { left: 58px; top: 808px; width: 382px; }
  .salad-right { left: 480px; top: 808px; width: 386px; }
  .salad-art {
    position: absolute; left: 276px; top: 1060px; width: 624px; height: 128px;
    border-radius: 50% 50% 8px 8px / 70% 70% 8px 8px;
    background: linear-gradient(180deg, rgba(143,174,106,0.9) 0%, #a9c07d 45%, #d6c8a0 100%);
  }
  .advisory {
    position: absolute; left: 40px; top: 1160px; width: 848px; text-align: center;
    font-size: 10.6px; line-height: 1.25; text-transform: uppercase; color: var(--ink);
  }
</style>
</head>
<body>
  <div class="brand">brookline diner &amp; tap</div>

  <div class="section-kicker">Signature</div>
  <h1 class="section-title">STEAK SELECTIONS</h1>

  <div class="column steak-left">
    <div class="item">
      <div class="item-head"><span>Santa Fe Ground Beef Steak!</span><span>$12.99</span></div>
      <p class="item-desc">12 oz. ground beef steak, topped with melting cheddar cheese, roasted peppers &amp; onions! (small portion 9.99)</p>
    </div>
    <div class="item">
      <div class="item-head"><span>Mushroom Gravy Ground Beef Steak</span><span>$12.99</span></div>
      <p class="item-desc">12 oz. ground beef steak topped with beef mushroom gravy (small portion 9.99)</p>
    </div>
    <div class="item">
      <div class="item-head"><span>Ribeye Steak</span><span>$14.99</span></div>
      <p class="item-desc">14 oz. rich flavor, juicy, well marbled. One of the most tender beef cuts!</p>
    </div>
    <div class="item">
      <div class="item-head"><span>Filet Mignon</span><span>$14.99</span></div>
      <p class="item-desc">8 oz. bacon wrapped. The most tender beef cut. Lean, buttery texture!</p>
    </div>
    <div class="item">
      <div class="item-head"><span>Kansas City Strip</span><span>$16.99</span></div>
      <p class="item-desc">16 oz. lean, tenderful, full flavored loin cut!</p>
    </div>
    <div class="item">
      <div class="item-head"><span>Chicken Fried Steak</span><span>$10.99</span></div>
      <p class="item-desc">Hand breaded &amp; fried and served with a choice of potato, country gravy &amp; house baked bread (small portion 9.99)</p>
    </div>
  </div>

  <div class="column steak-right">
    <div class="item">
      <div class="item-head"><span>Steak Del Rio</span><span>$16.99</span></div>
      <p class="item-desc">12 oz. choice tenderloin cut, rubbed with bold southern spices and topped with a dollop of chipotle butter and fried onion tanglers!</p>
    </div>
  </div>

  <div class="steak-art" role="img" aria-label="Watercolour illustration of grilled steaks and lamb chops with potatoes"></div>

  <div class="served-note">
    <svg width="28" height="18" viewBox="0 0 28 18" aria-hidden="true"><path d="M1 6h14V1l12 8-12 8v-5H1z" fill="var(--red)"/></svg>
    <span>All served with choice of potato<br>and homemade bread!</span>
  </div>

  <div class="band">SALAD SENSATION</div>
  <div class="salad-frame"></div>

  <div class="column salad-left">
    <div class="item">
      <div class="item-head"><span>Gourmet Salads</span><span>$8.99</span></div>
      <p class="item-desc">Choose from charbroiled chicken, fried chicken, or ham &amp; turkey on tossed iceberg lettuce, with carrots, red cabbage, cucumbers, tomatoes, boiled eggs, fried bacon, shredded cheeses, croutons &amp; garlic breadsticks! (small salads 7.99)</p>
    </div>
    <div class="item">
      <div class="item-head"><span>West Coast Salad</span><span>$8.99</span></div>
      <p class="item-desc">Blackened chicken breast or cocktail shrimp on romaine lettuce with bleau cheese crumbles, fresh pineapple, mandarin oranges, strawberries, blueberries, blackberries (in season), egg slices, tomatoes, and roasted almonds &amp; croutons! Served with fruit vinaigrette and a garlic breadstick! (small 7.99)</p>
    </div>
  </div>

  <div class="column salad-right">
    <div class="item">
      <div class="item-head"><span>Chicken Caesar Salad</span><span>$8.99</span></div>
      <p class="item-desc">Tossed romaine lettuce, charbroiled chicken, shredded parmesan cheese, diced tomatoes, home style croutons, creamy caesar dressing &amp; a garlic bread stick! (small 7.99)</p>
    </div>
    <div class="item">
      <div class="item-head"><span>Southwest Blackened Chicken Salad!</span><span>$8.99</span></div>
      <p class="item-desc">Blackened chicken breast on iceberg lettuce, with jack &amp; cheddar cheeses, tomatoes, avocado slices, black beans, black olives, sweet corn, sour cream, tortilla chips &amp; a wedge of lime with a special south-west dressing! (small 7.99)</p>
    </div>
  </div>

  <div class="salad-art" role="img" aria-label="Illustration of fresh salads with greens, tomatoes, cucumbers and peppers"></div>

  <p class="advisory">Consumer advisory: consuming raw or undercooked meat, poultry, seafood, shellfish or eggs may increase your risk of foodborne illness.<br>Sorry, we can't split small portions. Split order will be charged small portion price or 1/2 price plus $1 per person if small portion not offered.</p>
</body>
</html>
```